Marisol's Henna Party Invitation on March 20, 2026

I'd like to design an invitation that would be sent via text and posted on social media for my niece's henna party. The color scheme would be white, gold, and black. I want it to be elegant and classy. The font could be something like Rastanty Cortez. The party would be on March 20, 2026. It's a traditional and cultural type of party (pre-wedding party). I've attached some ideas for inspiration and to get a feel of a henna party.

Target Market(s)

This invitation would only be sent via text to our guests and posted on social media.

Font styles to use
Decorative
Script
Other font styles liked:
• Rastanty Cortez

Requirements
Must have
• Elegance, classy, a henna party reflection but something elegant and perhaps abstract.
Nice to have
• Something reflecting the henna party tradition. It could be a high gold candle, a decorated tray, etc. But I want it to be elegant and less crowded of an invitation.

```html
<!DOCTYPE html>
<html lang="en">
<head>
<meta charset="UTF-8">
<title>Henna Party Invitation</title>
<link href="https://fonts.googleapis.com/css2?family=Cinzel:wght@700&family=Pinyon+Script&family=Allison&family=Marcellus&display=swap" rel="stylesheet">
<style>
  :root {
    --paper: #fdfbfa;
    --paper-warm: #f7efea;
    --ink: #111111;
    --gold-pale: #fbf3cf;
    --gold-light: #f3e08a;
    --gold: #c9a23a;
    --gold-deep: #8f6a1c;
    --henna: #3c3c3c;
    --band: #050505;
  }
  * { margin: 0; padding: 0; box-sizing: border-box; }
  html, body { width: 800px; height: 1200px; overflow: hidden; background: var(--paper); }
  .invitation {
    position: relative;
    width: 800px;
    height: 1200px;
    overflow: hidden;
    background: radial-gradient(ellipse at 50% 50%, var(--paper-warm) 0%, var(--paper) 60%, #ffffff 100%);
  }
  .mandala {
    position: absolute;
    left: 109px;
    top: -262px;
    width: 580px;
    height: 580px;
    border-radius: 50%;
    background: radial-gradient(circle at 50% 50%,
      rgba(255,251,224,0.95) 0%,
      rgba(251,243,207,0.9) 30%,
      rgba(233,211,140,0.55) 55%,
      rgba(214,182,98,0.35) 72%,
      rgba(214,182,98,0.12) 88%,
      rgba(255,255,255,0) 100%);
  }
  .eyebrow {
    position: absolute;
    top: 330px;
    width: 100%;
    text-align: center;
    font-family: "Cinzel", serif;
    font-weight: 700;
    font-size: 26px;
    color: var(--ink);
  }
  .divider { position: absolute; left: 0; width: 100%; height: 30px; }
  .divider-line {
    position: absolute;
    top: 50%;
    height: 2px;
    background: linear-gradient(90deg, rgba(143,106,28,0), var(--gold-deep) 20%, var(--gold) 80%, rgba(201,162,58,0));
  }
  .divider-ornament {
    position: absolute;
    top: 50%;
    left: 50%;
    transform: translate(-50%, -50%);
    border-radius: 50%;
    background: radial-gradient(ellipse at 50% 50%, var(--gold-light) 0%, var(--gold) 45%, rgba(201,162,58,0.35) 75%, rgba(201,162,58,0) 100%);
  }
  .divider--top { top: 380px; }
  .divider--top .divider-line { left: 273px; width: 247px; }
  .divider--top .divider-ornament { width: 46px; height: 28px; }
  .divider--bottom { top: 702px; }
  .divider--bottom .divider-line { left: 137px; width: 519px; }
  .divider--bottom .divider-ornament { width: 96px; height: 62px; }
  .honoree {
    position: absolute;
    top: 422px;
    width: 100%;
    text-align: center;
    font-family: "Pinyon Script", cursive;
    font-size: 72px;
    line-height: 1;
    color: var(--ink);
  }
  .gold-text {
    background: linear-gradient(100deg, var(--gold-deep) 0%, var(--gold) 25%, var(--gold-light) 45%, var(--gold) 60%, var(--gold-deep) 80%, var(--gold) 100%);
    -webkit-background-clip: text;
    background-clip: text;
    color: transparent;
  }
  .title {
    position: absolute;
    top: 490px;
    width: 100%;
    text-align: center;
    font-family: "Allison", cursive;
    font-size: 180px;
    line-height: 1;
    font-weight: 400;
  }
  .date {
    position: absolute;
    top: 762px;
    width: 100%;
    text-align: center;
    font-family: "Allison", cursive;
    font-size: 96px;
    line-height: 1;
  }
  .henna-hands {
    position: absolute;
    left: 246px;
    top: 883px;
    width: 293px;
    height: 195px;
    border-radius: 50% 50% 20% 20% / 60% 60% 20% 20%;
    background: radial-gradient(ellipse at 50% 65%,
      rgba(60,60,60,0.55) 0%,
      rgba(60,60,60,0.38) 40%,
      rgba(60,60,60,0.15) 70%,
      rgba(60,60,60,0) 100%);
  }
  .footer-band {
    position: absolute;
    left: 0;
    top: 1078px;
    width: 800px;
    height: 122px;
    background: var(--band);
    border-bottom: 6px solid var(--gold);
    display: flex;
    align-items: center;
    justify-content: center;
  }
  .footer-band::before {
    content: "";
    position: absolute;
    left: 0; right: 0; top: 0; height: 13px;
    background: linear-gradient(180deg, var(--gold-light), var(--gold) 50%, var(--gold-deep));
  }
  .tagline {
    margin-top: 10px;
    font-family: "Marcellus", serif;
    font-size: 38px;
    letter-spacing: 1px;
  }
</style>
</head>
<body>
  <main class="invitation">
    <div class="mandala" role="img" aria-label="Gold line-art mandala ornament"></div>

    <p class="eyebrow">PLEASE JOIN US FOR</p>

    <div class="divider divider--top">
      <span class="divider-line"></span>
      <span class="divider-ornament" role="img" aria-label="Small gold flourish ornament"></span>
    </div>

    <p class="honoree">My Niece's</p>
    <h1 class="title gold-text">Henna Party</h1>

    <div class="divider divider--bottom">
      <span class="divider-line"></span>
      <span class="divider-ornament" role="img" aria-label="Gold scrollwork flourish ornament"></span>
    </div>

    <p class="date gold-text">March 20, 2026</p>

    <div class="henna-hands" role="img" aria-label="Illustration of two open hands decorated with henna patterns"></div>

    <footer class="footer-band">
      <p class="tagline gold-text">A Night of Tradition &amp; Celebration</p>
    </footer>
  </main>
</body>
</html>
```